Website Design for a High School

School Name: Bayt Qamarin Private Schools
sub-schools:
1-Bayt Qamarin Primary School
2-Bayt Qamarin High School for Girls
3-Bayt Qamarin High School for Boys
The design should be professional and serious and below is the details of the website.
Pages: (Home, About Us, Schools, Events, Students, Gallery, Lectures, Contact Us).
A-) Home Page:
1-Animated photos banner as main
2-Marquee for the last news.
3-Welcoming block of text
4-latest news at the body of the page.
5-Calender "on the side"
6-Number of visitors "on the side"
7-Search bar
8-options to choose a school
B-) School Page:
three schools listed as drop down menu when highlighted over the Schools button in the menu
*Each school page should contain:
1-Student login area
2-Animation photos header
3-Specific news and projects
C-) Student Login page:
have a Report Card
D-) Gallery Page
have a collection of photos.
E-)Contact Page
phone numbers
emails
feedback form
F-)Other mentioned pages
with normal text and photos page look as similar to the Home page.
Required color: Purple as main and include the logo colors
Logo: is attached.
Button link to change language to Arabic.

```html
<!DOCTYPE html>
<html lang="en">
<head>
<meta charset="utf-8">
<title>Bayt Qamarin Private Schools</title>
<link href="https://fonts.googleapis.com/css2?family=Open+Sans:wght@300;400;600;700&family=Ubuntu:wght@400;500;700&display=swap" rel="stylesheet">
<style>
:root{
  --purple:#5a2d91;
  --purple-deep:#3f1a72;
  --purple-bar:#6d4ba6;
  --purple-light:#7d5bb8;
  --yellow:#fdd866;
  --yellow-pale:#fff1b8;
  --yellow-deep:#f2b632;
  --ink:#4a4a4a;
  --white:#ffffff;
}
*{margin:0;padding:0;box-sizing:border-box}
html,body{width:852px;height:1200px;overflow:hidden;background:var(--white);font-family:"Open Sans",sans-serif;color:var(--ink)}
.page{position:relative;width:852px;height:1200px}
.top-band{position:absolute;left:0;top:0;width:852px;height:230px}
.search{position:absolute;left:70px;top:10px;width:201px;height:19px;border:1px solid #8b6cc0;background:#4f2788;color:#d8ccef;font-size:8.5px;padding:3px 9px}
.search svg{position:absolute;right:6px;top:4px}
.lang{position:absolute;left:757px;top:15px;font-size:7.5px;color:var(--white)}
.nav{position:absolute;left:70px;top:40px;width:712px;height:52px;background:linear-gradient(#fdd24f,#fff3c4);border-bottom:4px solid var(--yellow-deep)}
.nav a{position:absolute;top:17px;font-size:11.5px;color:#3a2a1a;text-decoration:none;font-weight:400}
.nav .sep{position:absolute;top:0;width:1px;height:52px;background:rgba(210,160,40,.35)}
.brand{position:absolute;left:388px;top:6px;width:77px;height:77px;border-radius:50%;background:var(--white);border:3px solid var(--purple-deep);display:flex;align-items:center;justify-content:center;text-align:center;font-family:"Ubuntu",sans-serif;font-weight:700;font-size:10px;line-height:1.2;color:var(--purple)}
.shadow{position:absolute;left:110px;top:92px;width:632px;height:14px;background:radial-gradient(ellipse at top,rgba(30,10,60,.45),transparent 70%)}
.hero{position:absolute;left:70px;top:111px;width:712px;height:396px;background:linear-gradient(100deg,#b9d27a 0%,#dfe9b8 40%,#e8dcc9 70%,#c9b39a 100%)}
.dots{position:absolute;left:80px;top:141px}
.dots span{display:block;width:7px;height:7px;border-radius:50%;background:var(--white);margin-bottom:5px}
.dots span:first-child{background:var(--purple)}
.hero-title{position:absolute;left:123px;top:316px;font-family:"Ubuntu",sans-serif;color:var(--purple);line-height:1.15}
.hero-title .light{font-weight:400;font-size:27px;display:block}
.hero-title .bold{font-weight:700;font-size:28px;display:block;color:#6a3aa6}
.tabs{position:absolute;left:70px;top:507px;width:712px;height:82px;display:flex;border-bottom:4px solid var(--yellow-deep)}
.tab{position:relative;height:78px;background:linear-gradient(#fdd24f,#fff2c0);display:flex;align-items:center;padding-left:12px}
.tab.active{background:linear-gradient(#f9bd2c,#fde08a)}
.tab .num{width:38px;height:38px;border-radius:50%;background:var(--purple-deep);border:2px solid #e9c560;color:var(--white);font-weight:700;font-size:14px;display:flex;align-items:center;justify-content:center;margin-right:10px}
.tab small{display:block;font-size:8px;color:var(--purple);font-weight:600}
.tab strong{display:block;font-family:"Ubuntu",sans-serif;font-size:14.5px;color:var(--purple);font-weight:700;line-height:1.1}
.news{position:absolute;left:70px;top:589px;width:712px;height:59px;background:var(--purple-bar);color:var(--white);display:flex;align-items:center}
.news .label{width:114px;height:59px;border-right:1px solid #5e3e96;display:flex;align-items:center;justify-content:center;font-family:"Ubuntu",sans-serif;font-weight:700;font-size:14px}
.news .date{margin-left:20px;font-style:italic;font-weight:700;color:var(--yellow);font-size:9.5px}
.news .text{margin-left:14px;font-size:10.5px;color:#efe8fa}
.welcome h1{position:absolute;left:70px;top:688px;font-family:"Ubuntu",sans-serif;font-weight:700;font-size:18.5px;color:var(--purple)}
.welcome-photo{position:absolute;left:70px;top:726px;width:465px;height:203px;background:linear-gradient(120deg,#7d9fb5,#c8b9a4 45%,#9fb6cc 100%)}
.welcome p{position:absolute;left:70px;top:934px;width:465px;font-size:10px;line-height:18.4px;color:#555}
.btn-more{position:absolute;left:70px;top:1021px;width:66px;height:20px;background:var(--yellow);color:var(--white);font-weight:700;font-size:9.5px;display:flex;align-items:center;justify-content:center}
.calendar{position:absolute;left:554px;top:693px;width:228px;height:188px;background:linear-gradient(var(--purple-light),var(--purple-deep));border-bottom:3px solid #2f1058;color:var(--white)}
.side-title{position:absolute;left:16px;top:12px;font-family:"Ubuntu",sans-serif;font-weight:700;font-size:14.5px;display:flex;align-items:center;gap:7px}
.calendar .month{position:absolute;top:40px;width:100%;text-align:center;font-weight:700;font-size:10px}
.calendar table{position:absolute;left:38px;top:60px;width:153px;border-collapse:collapse;font-size:7.5px;text-align:center}
.calendar th{font-size:6.5px;font-weight:600;padding:2px 0 4px;border-top:1px solid #9a80c9;border-bottom:1px solid #9a80c9}
.calendar td{padding:4px 0 4.3px;font-weight:600}
.calendar td.sun{color:var(--yellow)}
.calendar tr:nth-child(2) td{padding-top:10px}
.visitors{position:absolute;left:554px;top:887px;width:228px;height:67px;background:linear-gradient(#fff0bb,#fdd45a);border-bottom:3px solid var(--yellow-deep)}
.visitors .side-title,.choose .side-title{color:var(--purple)}
.visitors .count{position:absolute;left:18px;top:34px;font-family:"Ubuntu",sans-serif;font-weight:700;font-size:14.5px;color:var(--white)}
.choose{position:absolute;left:554px;top:963px;width:228px;height:75px;background:linear-gradient(#fff0bb,#fdd45a);border-bottom:3px solid var(--yellow-deep)}
.select{position:absolute;left:14px;top:37px;width:201px;height:22px;background:#fcc94a;border:1px solid #f0c040;font-size:8px;color:#fff6d5;padding:5px 10px}
.select svg{position:absolute;left:152px;top:7px}
.go{position:absolute;left:168px;top:3px;width:28px;height:15px;border-radius:8px;background:var(--purple-deep);color:var(--white);font-size:8px;display:flex;align-items:center;justify-content:center}
.footer-band{position:absolute;left:0;top:1078px}
.social{position:absolute;top:1105px;left:362px;display:flex;gap:4px}
.social span{width:23px;height:23px;border-radius:50%;border:1.3px solid var(--white)}
.footer-links{position:absolute;top:1142px;width:852px;text-align:center;font-size:10px;color:var(--white);word-spacing:2px}
.footer-links span{margin:0 9px}
.copy{position:absolute;top:1165px;width:852px;text-align:center;font-size:9.5px;color:var(--white)}
</style>
</head>
<body>
<div class="page">
  <svg class="top-band" viewBox="0 0 852 230" aria-hidden="true">
    <path d="M0 0H852V222Q426 200 0 222Z" fill="var(--purple)"/>
  </svg>

  <div class="search">Search
    <svg width="9" height="9" viewBox="0 0 10 10"><circle cx="4" cy="4" r="3" fill="none" stroke="#f2b632" stroke-width="1.5"/><path d="M6.3 6.3L9 9" stroke="#f2b632" stroke-width="1.6"/></svg>
  </div>
  <div class="lang">EN | AR</div>

  <nav class="nav">
    <a style="left:24px">Home</a><i class="sep" style="left:69px"></i>
    <a style="left:85px">About Us</a><i class="sep" style="left:145px"></i>
    <a style="left:160px">Schools</a><i class="sep" style="left:214px"></i>
    <a style="left:228px">Events</a><i class="sep" style="left:276px"></i>
    <i class="sep" style="left:436px"></i>
    <a style="left:438px">Students</a><i class="sep" style="left:498px"></i>
    <a style="left:512px">Gallery</a><i class="sep" style="left:562px"></i>
    <a style="left:577px">Lectures</a><i class="sep" style="left:636px"></i>
    <a style="left:649px">Contact Us</a>
  </nav>
  <div class="brand">Bayt<br>Qamarin</div>
  <div class="shadow"></div>

  <div class="hero" role="img" aria-label="Photo of a smiling student holding a book outdoors on a school campus"></div>
  <div class="dots"><span></span><span></span><span></span><span></span></div>
  <div class="hero-title"><span class="light">Bayt Qamarin</span><span class="bold">High School for Girls</span></div>

  <div class="tabs">
    <div class="tab" style="width:228px"><div class="num">1</div><div><small>Bayt Qamarin</small><strong>Primary School</strong></div></div>
    <div class="tab active" style="width:239px"><div class="num">2</div><div><small>Bayt Qamarin</small><strong>High School for Girls</strong></div></div>
    <div class="tab" style="width:245px"><div class="num">3</div><div><small>Bayt Qamarin</small><strong>High School for Boys</strong></div></div>
  </div>

  <div class="news">
    <div class="label">Last News</div>
    <div class="date">May 15th 2015</div>
    <div class="text">Neque porro quisquam est qui dolorem ipsum quia dolor sit amet, consectetur, adipisci velit...</div>
  </div>

  <section class="welcome">
    <h1>WELCOME TO BAYT QAMARIN SCHOOLS</h1>
    <div class="welcome-photo" role="img" aria-label="Photo of students writing at desks in a classroom"></div>
    <p>Lorem Ipsum is simply dummy text of the printing and typesetting industry. Lorem Ipsum has been the industry's standard dummy text ever since the 1500s, when an unknown printer took a galley of type and scrambled it to make a type specimen book. It has survived not only five centuries, but also the leap into electronic typesetting, remaining essentially unchanged.</p>
    <div class="btn-more">Read More</div>
  </section>

  <aside class="calendar">
    <div class="side-title"><svg width="14" height="14" viewBox="0 0 14 14"><rect x="1" y="2" width="12" height="11" fill="none" stroke="#fff" stroke-width="1.4"/><path d="M1 5.5H13M4 0.5V3.5M10 0.5V3.5" stroke="#fff" stroke-width="1.4"/></svg>Calendar</div>
    <div class="month">SEPTEMBER</div>
    <table>
      <tr><th>SUN</th><th>MON</th><th>TUE</th><th>WED</th><th>THU</th><th>FRI</th><th>SAT</th></tr>
      <tr><td class="sun">28</td><td>29</td><td>30</td><td>31</td><td>1</td><td>2</td><td>3</td></tr>
      <tr><td class="sun">4</td><td>5</td><td>6</td><td>7</td><td>8</td><td>9</td><td>10</td></tr>
      <tr><td class="sun">11</td><td>12</td><td>13</td><td>14</td><td>15</td><td>16</td><td>17</td></tr>
      <tr><td class="sun">18</td><td>19</td><td>20</td><td>21</td><td>22</td><td>23</td><td>24</td></tr>
      <tr><td class="sun">25</td><td>26</td><td>27</td><td>28</td><td>29</td><td>30</td><td>1</td></tr>
    </table>
  </aside>

  <aside class="visitors">
    <div class="side-title"><svg width="13" height="13" viewBox="0 0 13 13"><circle cx="6.5" cy="4" r="3" fill="#fff"/><path d="M1 13Q1 7.5 6.5 7.5T12 13Z" fill="#fff"/></svg>Number of visitors</div>
    <div class="count">1,38,382,928 &nbsp;Visited</div>
  </aside>

  <aside class="choose">
    <div class="side-title"><svg width="12" height="14" viewBox="0 0 12 14"><rect x="1" y="1" width="10" height="13" fill="#fff"/><path d="M3 3H5M7 3H9M3 6H5M7 6H9M3 9H5M7 9H9" stroke="#fcc94a" stroke-width="1.2"/></svg>Choose Your School</div>
    <div class="select">Your School
      <svg width="8" height="6" viewBox="0 0 8 6"><path d="M1 1L4 4L7 1" fill="none" stroke="#fff" stroke-width="1.4"/></svg>
      <div class="go">GO</div>
    </div>
  </aside>

  <svg class="footer-band" width="852" height="122" viewBox="0 0 852 122" aria-hidden="true">
    <path d="M0 34Q426 -14 852 34V122H0Z" fill="var(--purple)"/>
  </svg>
  <div class="social" aria-label="Social links"><span></span><span></span><span></span><span></span><span></span></div>
  <div class="footer-links">Home<span>|</span>About Us<span>|</span>Schools<span>|</span>Events<span>|</span>Students<span>|</span>Gallery<span>|</span>Lectures<span>|</span>Contact Us</div>
  <div class="copy">© 2015 Company Name ,All Rights Reserved</div>
</div>
</body>
</html>
```